I would like to update my one-page service sheet to provide a more professional/polished look and...

One page service sheet - with content on both the front and back. I've uploaded my current one page service sheet to provide background. I've also included a service sheet that I recently received from another business owner (from a very different business) that is a representation of the kind of feel I'm looking for. My business website may be found at: www.morvitelconsulting.com

```html
<!DOCTYPE html>
<html lang="en">
<head>
<meta charset="utf-8">
<title>Growth Services Sheet</title>
<link href="https://fonts.googleapis.com/css2?family=Montserrat:ital,wght@0,400;0,500;0,600;0,700;1,400&display=swap" rel="stylesheet">
<style>
  :root {
    --navy: #2c3a4b;
    --orange: #f26b21;
    --paper-light: #f7f7f8;
    --paper-mid: #e9eaec;
    --body: #33373d;
  }
  * { margin: 0; padding: 0; box-sizing: border-box; }
  html, body { width: 927px; height: 1200px; overflow: hidden; }
  body {
    position: relative;
    font-family: "Montserrat", Arial, sans-serif;
    color: var(--body);
    background: linear-gradient(180deg, var(--paper-light) 0%, var(--paper-mid) 50%, var(--paper-light) 100%);
  }
  .service-block { position: absolute; }
  .service-block.left { left: 28px; width: 452px; }
  .service-block.right { right: 27px; width: 420px; text-align: right; }
  .kicker {
    font-size: 24px; font-weight: 400; letter-spacing: 0.2px; line-height: 1.05;
  }
  .headline {
    font-size: 34px; font-weight: 700; letter-spacing: 0.5px; line-height: 1.1;
  }
  .kicker-navy .kicker { color: var(--navy); }
  .kicker-navy .headline { color: var(--orange); }
  .kicker-orange .kicker { color: var(--orange); }
  .kicker-orange .headline { color: var(--navy); }
  .tagline {
    margin-top: 10px; font-size: 16.5px; font-style: italic; line-height: 1.22; color: var(--navy);
  }
  .rule { height: 5px; background: var(--orange); margin-top: 7px; }
  .service-list { list-style: none; margin-top: 17px; }
  .service-list li {
    font-size: 14.6px; line-height: 1.24; margin-bottom: 16px; color: var(--body);
  }
  .service-list strong { font-weight: 600; color: var(--navy); }
  .right .service-list strong { color: var(--orange); }
  .photo { position: absolute; }
  .photo-ideas { left: 503px; top: 0; width: 424px; height: 380px;
    background: linear-gradient(135deg, #d8d8d6 0%, #bfc0bd 45%, #5a7fc4 55%, #cfd0cd 70%, #a9aaa6 100%); }
  .photo-partners { left: 0; top: 405px; width: 437px; height: 392px;
    background: radial-gradient(ellipse at 50% 45%, #8f9a80 0%, #6b7660 55%, #4d5646 100%); }
  .photo-trading { left: 503px; top: 824px; width: 424px; height: 376px;
    background: linear-gradient(160deg, #8a6a78 0%, #b4b6ba 30%, #e8e8ea 50%, #a5a7ab 70%, #9a6b4a 100%); }
</style>
</head>
<body>
  <section class="service-block left kicker-navy" style="top:24px;">
    <h2><span class="kicker" style="display:block;">GROWTH STRATEGY</span><span class="headline" style="display:block;">&amp; INNOVATION</span></h2>
    <p class="tagline">Discover what’s needed to reach<br>the next stage of growth.</p>
    <div class="rule"></div>
    <ul class="service-list">
      <li><strong>Growth Strategy &amp; Business Model Review.</strong> Gain an objective perspective on your growth strategy and business.</li>
      <li><strong>Revenue Acceleration &amp; Lead Generation.</strong> Define and execute strategies and tactics to drive demand and top line growth.</li>
      <li><strong>Execution and Scale.</strong> Enable your people, processes, and technology to meet the demands of growth.</li>
      <li><strong>Pricing Strategies.</strong> Strategically price products and services.</li>
      <li><strong>Growth Training.</strong> Group and individual training/coaching.</li>
    </ul>
  </section>

  <div class="photo photo-ideas" role="img" aria-label="Photo of a crumpled blue paper ball on a notebook with lightbulb sketches"></div>

  <div class="photo photo-partners" role="img" aria-label="Chalkboard drawing of a handshake above the word Partners"></div>

  <section class="service-block right kicker-orange" style="top:404px;">
    <h2><span class="kicker" style="display:block;">GROWTH PROCESS</span><span class="headline" style="display:block;">&amp; EXECUTION</span></h2>
    <p class="tagline">Fine-tune and formalize growth processes<br>for efficiency, effectiveness, and scale.</p>
    <div class="rule" style="margin-left:-44px;"></div>
    <ul class="service-list">
      <li><strong>Innovation Capture &amp; Elaboration.</strong> Standardize idea capture, analysis, funding, elaboration, and innovation roll-out.</li>
      <li><strong>Growth Channel Optimization.</strong> Enhance the prospect and customer experience by blending digital and traditional.</li>
      <li><strong>Business Development.</strong> Transform business development into a proactive “team sport” and increase accountability.</li>
      <li><strong>Prospect &amp; Client Experience Mapping.</strong> Create greater client stickiness, brand resonance, and be “easier to do business with.”</li>
    </ul>
  </section>

  <section class="service-block left kicker-orange" style="top:818px;">
    <h2><span class="kicker" style="display:block;">GROWTH SOLUTIONS</span><span class="headline" style="display:block;">&amp; ANALYTICS</span></h2>
    <p class="tagline">Get the right capabilities in place<br>to support your growth journey</p>
    <div class="rule"></div>
    <ul class="service-list">
      <li><strong>Technology Strategy &amp; Roadmap.</strong> Ensure that the right technology is in place for each step of your growth journey.</li>
      <li><strong>Software Selection.</strong> Identify the specific capabilities and vendors that are most appropriate for your business.</li>
      <li><strong>Project Leadership.</strong> Get critical projects over the finish line.</li>
      <li><strong>Disruptive Trends.</strong> Demystify “Digital,” “Big Data,” “Artificial Intelligence,” and “Internet of Things” to create advantage.</li>
      <li><strong>Critical Metrics.</strong> Determine the leading and lagging metrics that are most critical for your business</li>
    </ul>
  </section>

  <div class="photo photo-trading" role="img" aria-label="Photo of hands holding a smartphone showing stock prices above a laptop keyboard"></div>
</body>
</html>
```